Lantern Airfields Homepage Design Update

here's the current site - http://lanternairfields.example/

client is not happy with overall look.

keeping the same info - intro text, headlines, featured media excepts and general navigation options - can you come up with a nicer, slicker look for this homepage?

UPDATE: since it was asked by designer.. the general layout doesnt have to be the same. its not required to have a big image, with text below that and then smaller images/text below that. as long as we have the same content on the page, it can organized and designed in any way,

client like big images, so one way or the other, keep that... but feel free to reorganize content, explore different ways of framing it, and/or anything else. make this homepage pop!

for the designer that wins this, we'll start an additional project to update the interior.

let me know if any questions..

thanks!

marcus

Target Market(s)

aviation industry professionals, local governments, general public

Number of Pages Required

1 page

Font styles to use
Sans Serif

Requirements
Must have
• big image somewhere. same content as on current site, just designed differently.

```html
<!DOCTYPE html>
<html lang="en">
<head>
<meta charset="utf-8">
<title>Lantern Airfields</title>
<link rel="stylesheet" href="https://fonts.googleapis.com/css2?family=Montserrat:wght@400;500;600;700;800&display=swap">
<style>
:root{
  --brand:#2d4f8e;
  --brand-dark:#223e73;
  --ink:#333;
  --muted:#9a9a9a;
  --nav:#7a7a7a;
  --rule:#9fd0ea;
  --footer:#6b6b6b;
  --white:#fff;
}
*{box-sizing:border-box;margin:0;padding:0}
html,body{width:1001px;height:1200px;overflow:hidden;background:var(--white);font-family:'Montserrat',sans-serif;color:var(--ink)}
.page{position:relative;width:1001px;height:1200px}

.site-header{position:absolute;top:0;left:0;width:100%;height:48px;background:var(--white);border-bottom:1px solid #e6e6e6}
.brand{position:absolute;left:200px;top:15px;display:flex;align-items:center;gap:7px;font-size:13px;font-weight:500;color:var(--brand)}
.brand-dot{width:12px;height:12px;border-radius:50%;background:var(--brand)}
.main-nav{position:absolute;right:201px;top:19px;display:flex;gap:9px;font-size:7.6px;font-weight:700;letter-spacing:.4px}
.main-nav a{color:var(--nav);text-decoration:none}
.main-nav a.is-active{color:var(--brand)}

.hero{position:absolute;top:48px;left:0;width:100%;height:546px;background:linear-gradient(180deg,#2f4763 0%,#6f7682 28%,#b7a48e 55%,#8f8a86 78%,#4e5767 100%)}
.hero-panel{position:absolute;left:186px;top:100px;width:629px;height:138px;background:rgba(60,60,60,.55);text-align:center;color:var(--white)}
.hero-title{margin-top:24px;font-size:29px;font-weight:800;line-height:31px;letter-spacing:1.6px;text-transform:uppercase}
.hero-sub{margin-top:13px;font-size:21px;font-weight:700}
.hero-cta{position:absolute;left:376px;top:364px;width:249px;height:52px;background:var(--brand);border:1.5px solid var(--white);border-radius:5px;color:var(--white);font-size:15px;font-weight:700;display:flex;align-items:center;justify-content:center}
.scroll-down{position:absolute;left:491px;top:515px}

.social{position:absolute;right:14px;top:225px;display:flex;flex-direction:column;gap:4px}
.social span{display:block;width:26px;height:26px;border:1.5px solid var(--white);border-radius:50%;position:relative}
.social svg{position:absolute;left:5px;top:6px}

.intro{position:absolute;top:633px;left:200px;width:601px}
.intro h1{text-align:center;font-size:15px;font-weight:700;color:var(--brand);line-height:17px;letter-spacing:.6px}
.intro p{margin-top:23px;font-size:8.7px;line-height:16.2px;letter-spacing:.3px;color:#444}
.divider{position:absolute;top:789px;left:200px;width:601px;height:1.5px;background:var(--rule)}

.carousel-arrow{position:absolute;top:953px}
.cards{position:absolute;top:836px;left:200px;display:flex;gap:17px}
.card{width:189px;height:252px;border:1px solid #ddd;box-shadow:0 2px 0 #eee,0 4px 0 #e4e4e4;background:var(--white);text-align:center}
.card-media{margin:1px;height:102px}
.card h2{margin-top:17px;font-size:12.5px;font-weight:500;color:#222}
.card p{margin:8px auto 0;width:160px;font-size:8.4px;line-height:15px;color:var(--muted)}
.card-btn{display:inline-block;margin-top:14px;width:75px;height:21px;line-height:21px;border-radius:4px;background:var(--brand);color:var(--white);font-size:8.4px;font-weight:600}
.dots{position:absolute;top:1116px;left:479px;display:flex;gap:9px}
.dots i{width:8px;height:8px;border-radius:50%;background:#999}
.dots i.is-current{background:var(--brand)}

.site-footer{position:absolute;bottom:0;left:0;width:100%;height:32px;background:var(--footer);color:var(--white);font-size:8.4px;text-align:center;line-height:32px}
</style>
</head>
<body>
<div class="page">
  <header class="site-header">
    <div class="brand"><span class="brand-dot"></span>Lantern Airfields</div>
    <nav class="main-nav">
      <a class="is-active" href="#">ABOUT</a><a href="#">SERVICES</a><a href="#">AIRPORTS</a><a href="#">NEWS &amp; MEDIA</a><a href="#">CONTACT</a><a href="#">EMPLOYEES</a>
    </nav>
  </header>

  <section class="hero" role="img" aria-label="Passenger jet taking off through golden clouds">
    <div class="hero-panel">
      <div class="hero-title">Bringing private, free<br>enterprise business practices</div>
      <div class="hero-sub">To airports throughout the U.S.</div>
    </div>
    <div class="hero-cta">READ MORE</div>
    <svg class="scroll-down" width="19" height="19" viewBox="0 0 19 19"><circle cx="9.5" cy="9.5" r="9" fill="#fff"/><path d="M5.5 7.5l4 4 4-4" stroke="#8a8a8a" stroke-width="2.2" fill="none"/></svg>
  </section>

  <div class="social">
    <span aria-label="Social profile"></span>
    <span aria-label="Email"><svg width="13" height="10" viewBox="0 0 13 10"><rect x=".5" y=".5" width="12" height="9" fill="#fff"/><path d="M.5 .5l6 5 6-5" stroke="#555" fill="none"/></svg></span>
    <span aria-label="Social profile"></span>
    <span aria-label="Social profile"></span>
  </div>

  <section class="intro">
    <h1>WE DEVELOP P3 AIRPORT OPPORTUNITIES<br>WITHIN THE U.S. MARKET</h1>
    <p>Lantern Airfields is focused on opportunities to invest, develop and manage both general aviation and commercial service airports in key U.S. markets. A subsidiary of Beacon Ridge Investments, a private equity firm that exclusively invests in the Aerospace &amp; Transportation sectors, Lantern has the resources available to invest and finance transactions.<br>Lantern maintains offices in New York, Dublin and Atlanta.</p>
  </section>
  <div class="divider"></div>

  <svg class="carousel-arrow" style="left:151px" width="12" height="20" viewBox="0 0 12 20"><path d="M10 2L3 10l7 8" stroke="#999" stroke-width="2.4" fill="none"/></svg>
  <div class="cards">
    <article class="card">
      <div class="card-media" role="img" aria-label="Bomber aircraft flying over clouds and deep blue sea" style="background:linear-gradient(180deg,#1e4fb4,#2f66c9 60%,#9cb7e0)"></div>
      <h2>WHO WE ARE</h2>
      <p>Donec ullamcorper sem id sapien ultricies dapibus. Ut eleifend purus sed nulla fermentum, a efficitur velit eleifend.</p>
      <span class="card-btn">Read More</span>
    </article>
    <article class="card">
      <div class="card-media" role="img" aria-label="Fighter jet in a clear blue sky" style="background:linear-gradient(180deg,#4f7dbf,#4a78bb)"></div>
      <h2>WHAT WE DO</h2>
      <p>Donec ullamcorper sem id sapien ultricies dapibus. Ut eleifend purus sed nulla fermentum, a efficitur velit eleifend.</p>
      <span class="card-btn">Read more</span>
    </article>
    <article class="card">
      <div class="card-media" role="img" aria-label="Airliner wing above the horizon" style="background:linear-gradient(180deg,#0d4f9c,#3a86cf 60%,#d8e6f2)"></div>
      <h2>WHY WE DO IT</h2>
      <p>Donec ullamcorper sem id sapien ultricies dapibus. Ut eleifend purus sed nulla fermentum, a efficitur velit eleifend.</p>
      <span class="card-btn">Read More</span>
    </article>
  </div>
  <svg class="carousel-arrow" style="left:843px" width="12" height="20" viewBox="0 0 12 20"><path d="M2 2l7 8-7 8" stroke="#2d4f8e" stroke-width="2.4" fill="none"/></svg>
  <div class="dots"><i class="is-current"></i><i></i><i></i></div>

  <footer class="site-footer">Copyright 2015 Lantern Airfields. All right reserved.</footer>
</div>
</body>
</html>
```